Waterjet Cutting Business requires an up to date website

We currently have a website which is outdated and in need of modernization.
We are only looking for a simple website with around 4 pages: Home, Contact Us, Materials, Gallery.
We have some pictures and a logo which can be used.
Our primary business is profile cutting of materials to customers specifications using high-pressure water with abrasive.
We are looking for creative ideas and are open to suggestions!
http://brightfordcutworks.com/index.asp?pid=1
Update:
Cut quality picture (uploaded)
Map
Comparison to other profile cutting methods such as plasma/laser
Single page style without continuous scrolling
"We can cut virtually any material from any drawing whether it be a Full 3D cad models to hand sketched "
Target Market(s)
Film Industry, Prototype, Engineering, Architect, Artisits, one off designs
Industry/Entity Type
Engineering
Number of Pages Required
1 page
Font styles to use
Look and feel

```html
<!DOCTYPE html>
<html lang="en">
<head>
<meta charset="utf-8">
<title>Brightford Cutworks</title>
<link href="https://fonts.googleapis.com/css2?family=Michroma&family=Roboto:wght@400;500;700&display=swap" rel="stylesheet">
<style>
:root{
  --blue:#1b5b82;
  --blue-dark:#15496b;
  --orange:#f08a3c;
  --ink:#222;
  --grey-bg:#f4f4f4;
  --text:#3a3a3a;
  --white:#fff;
}
*{box-sizing:border-box;margin:0;padding:0}
html,body{width:1200px;height:3409px;overflow:hidden}
body{position:relative;background:var(--white);font-family:"Roboto",Arial,sans-serif;color:var(--text)}
.abs{position:absolute}
.display{font-family:"Michroma",sans-serif;text-transform:uppercase;letter-spacing:2px}
.brand{display:flex;align-items:center;gap:12px;font-family:"Michroma",sans-serif;color:var(--blue);font-size:26px;text-transform:uppercase;letter-spacing:1px}
.brand-mark{width:22px;height:22px;border-radius:50%;background:var(--blue)}
.site-header{top:0;left:0;width:1200px;height:141px;background:var(--white);display:flex;justify-content:center;align-items:center}
.menu-toggle{position:absolute;left:1050px;top:60px;width:28px}
.menu-toggle span{display:block;height:4px;background:var(--blue);margin-bottom:5px;border-radius:1px}
.hero{top:141px;left:0;width:1200px;height:666px;clip-path:polygon(0 0,100% 0,100% 66%,31% 100%,0 91%);background:linear-gradient(135deg,#0d1b1f 0%,#2b4a50 45%,#5d7d84 70%,#1e2f33 100%)}
.hero-title{top:440px;left:0;width:1200px;text-align:center;color:var(--white);font-size:27px;line-height:34px}
.hero-play{top:534px;left:582px}
.hero-arrow{top:460px}
.section-title{font-size:26px;color:var(--ink)}
.materials-frame{left:91px;top:920px;width:409px;height:319px;border:14px solid var(--blue)}
.materials-photo{left:136px;top:970px;width:409px;height:307px;background:linear-gradient(140deg,#3b1a55 0%,#c02a9e 45%,#f06fd2 60%,#5a2274 100%)}
.materials-copy{left:598px;top:888px;width:486px}
.materials-sub{font-size:16px;line-height:20px;color:var(--ink);margin:30px 0 16px}
.materials-copy p{font-size:14.5px;line-height:19px;margin-bottom:16px}
.btn-outline{display:inline-flex;justify-content:center;align-items:center;width:166px;height:35px;border:2px solid var(--orange);border-radius:18px;font-size:14px;color:var(--ink)}
.gallery-title{left:175px;top:1555px}
.tile{position:absolute}
.testimonials-head{top:2232px;left:0;width:1200px;text-align:center}
.testimonials-head p{font-size:14px;margin-top:8px}
.testimonial-photo{left:209px;top:2325px;width:398px;height:296px;background:linear-gradient(140deg,#2a1640 0%,#b52a9a 45%,#f07ad6 58%,#47204f 100%)}
.testimonial-card{left:607px;top:2348px;width:404px;height:250px;background:var(--grey-bg)}
.avatar{left:537px;top:2403px;width:154px;height:154px;border-radius:50%;border:5px solid var(--white);background:linear-gradient(160deg,#c7b9aa,#6f5a4a)}
.quote{left:700px;top:2398px;width:290px;text-align:center}
.quote h3{font-size:17px;color:var(--ink);font-weight:400}
.quote .role{color:var(--blue);font-size:13px;font-weight:500;margin:6px 0 10px}
.quote p{font-size:13px;line-height:18px;padding:0 30px;position:relative}
.quote .mark{position:absolute;font-size:26px;font-family:Georgia,serif;color:var(--ink)}
.stars{color:var(--orange);font-size:15px;letter-spacing:3px;margin-top:6px}
.dots{display:flex;justify-content:center;gap:5px;margin-top:8px}
.dots span{width:7px;height:7px;border-radius:50%;background:#bbb}
.dots span:first-child{background:var(--blue-dark)}
.newsletter{top:2762px;left:0;width:1200px;text-align:center}
.newsletter h2{font-size:23px;color:var(--ink)}
.newsletter p{font-size:14px;margin-top:8px}
.signup{position:absolute;left:332px;top:2835px;width:511px;height:29px;border-radius:15px;background:#efefef;display:flex;overflow:hidden}
.signup .field{flex:1;font-size:12px;color:#777;padding:8px 18px}
.signup .submit{width:129px;background:var(--orange);color:var(--white);font-size:12px;display:flex;align-items:center;justify-content:center;border-radius:15px}
.footer-brand{top:2920px;left:0;width:1200px;display:flex;justify-content:center}
.contact-icon{width:60px;height:60px;border-radius:50%;background:var(--orange);display:flex;align-items:center;justify-content:center}
.contact-text{color:var(--white);font-size:14px;line-height:19px;text-align:center}
.quick-title{top:3232px;left:0;width:1200px;text-align:center;color:var(--orange);font-size:17px}
.footer-nav{top:3268px;left:0;width:1200px;height:22px;color:var(--white);font-size:14px;font-weight:500}
.footer-nav span{position:absolute}
.bottom-bar{top:3359px;left:0;width:1200px;height:50px;background:var(--orange);color:var(--white);font-size:14px;display:flex;align-items:center;padding-left:120px}
.social{position:absolute;top:12px;width:27px;height:27px;border-radius:50%;background:var(--white)}
</style>
</head>
<body>

<svg class="abs" style="left:0;top:0" width="1200" height="3409" aria-hidden="true">
  <polygon points="0,1341 830,1546 1200,1432 1200,2262 477,2080 0,2228" fill="#f4f4f4"/>
  <polygon points="0,2960 818,3046 1200,2912 1200,3409 0,3409" fill="#1b5b82"/>
</svg>

<header class="site-header abs">
  <div class="brand"><span class="brand-mark"></span>Brightford Cutworks</div>
  <div class="menu-toggle"><span></span><span></span><span></span></div>
</header>

<section class="hero abs" role="img" aria-label="Waterjet cutting head working over a metal sheet"></section>
<h1 class="hero-title abs display">Welcome to<br>Brightford Cutworks</h1>
<svg class="hero-arrow abs" style="left:42px" width="26" height="28" aria-hidden="true"><polygon points="23,3 23,25 4,14" fill="none" stroke="#fff" stroke-width="3"/></svg>
<svg class="hero-arrow abs" style="left:1112px" width="26" height="28" aria-hidden="true"><polygon points="3,3 3,25 22,14" fill="none" stroke="#f08a3c" stroke-width="3"/></svg>
<svg class="hero-play abs" width="36" height="36" aria-hidden="true"><circle cx="18" cy="18" r="15" fill="none" stroke="#fff" stroke-width="3"/><polygon points="14,11 14,25 25,18" fill="#fff"/></svg>

<div class="materials-frame abs"></div>
<div class="materials-photo abs" role="img" aria-label="Waterjet nozzle cutting sheet material under pink light"></div>
<section class="materials-copy abs">
  <h2 class="section-title display">Materials</h2>
  <h3 class="materials-sub display">It is possible to cut virtually<br>any profile in any material<br>with waterjet</h3>
  <p>Materials we can cut include, but are not limited to, all metals and alloys, stone and ceramics, composites, solid surface, wood, glass, acrylics, resins, silicones, plastics, foams, carpet and felts. We can also cut laminated dissimilar materials which can often be very hard to cut using conventional methods. We are always happy to test cut a sample of your material free of charge to demonstrate the quality of cut achievable.</p>
  <p>Employing Streamline's low pressure vacuum assist we can pierce and cut brittle materials such as acrylics,and ceramics. In addition Adaptive Jet technology.</p>
  <span class="btn-outline">Read More</span>
</section>

<h2 class="gallery-title abs section-title display">Gallery</h2>
<div class="tile" style="left:123px;top:1623px;width:229px;height:377px;background:linear-gradient(150deg,#1f8fa8,#6b4a3a 70%,#3a7f95)" role="img" aria-label="Waterjet cut metal gears"></div>
<div class="tile" style="left:364px;top:1623px;width:231px;height:184px;background:linear-gradient(135deg,#f2f2f2,#9a9694)" role="img" aria-label="Cut metal bracket part"></div>
<div class="tile" style="left:364px;top:1818px;width:231px;height:182px;background:linear-gradient(135deg,#a58a4e,#d8c08a)" role="img" aria-label="Cut cork discs"></div>
<div class="tile" style="left:607px;top:1623px;width:231px;height:377px;background:linear-gradient(160deg,#2a6d9a,#1b5b82)" role="img" aria-label="Waterjet machine in blue tone"></div>
<div class="tile" style="left:850px;top:1623px;width:232px;height:184px;background:linear-gradient(135deg,#f4f4f4,#c9c9c9)" role="img" aria-label="Cut metal spiral profiles"></div>
<div class="tile" style="left:850px;top:1818px;width:232px;height:182px;background:linear-gradient(135deg,#f0f0f0,#b8824f 60%,#e4e4e4)" role="img" aria-label="Cut brass and steel wheels"></div>
<span class="btn-outline abs" style="left:882px;top:2055px">View More</span>

<section class="testimonials-head abs">
  <h2 class="section-title display">Testimonials</h2>
  <p>Lorem Ipsum is simply dummy text of the printing industry.</p>
</section>
<div class="testimonial-photo abs" role="img" aria-label="Waterjet cutting head at work under pink light"></div>
<div class="testimonial-card abs"></div>
<div class="avatar abs" role="img" aria-label="Client portrait"></div>
<div class="quote abs">
  <h3 class="display">Daniel Hart</h3>
  <div class="role">Creative Director</div>
  <p><span class="mark" style="left:6px;top:-10px">&ldquo;</span>Lorem Ipsum &nbsp;simply dummy text the printing and ypesetting industry Ipsum is simply dummy text of the printing.<span class="mark" style="right:6px;bottom:-14px">&rdquo;</span></p>
  <div class="stars">★★★★★</div>
  <div class="dots"><span></span><span></span><span></span></div>
</div>

<section class="newsletter abs">
  <h2 class="display">Join the Newletter</h2>
  <p>Sign up for Our Newsletter</p>
</section>
<div class="signup"><span class="field">Email here</span><span class="submit">Subscribe</span></div>

<div class="footer-brand abs"><div class="brand"><span class="brand-mark"></span>Brightford Cutworks</div></div>

<div class="contact-icon abs" style="left:256px;top:3091px"><svg width="28" height="28" viewBox="0 0 24 24" aria-hidden="true"><path d="M6.6 10.8a15.1 15.1 0 0 0 6.6 6.6l2.2-2.2c.3-.3.7-.4 1-.2 1.1.4 2.3.6 3.6.6.6 0 1 .4 1 1V20c0 .6-.4 1-1 1A17 17 0 0 1 3 4c0-.6.4-1 1-1h3.5c.6 0 1 .4 1 1 0 1.3.2 2.5.6 3.6.1.3 0 .7-.2 1z" fill="#fff"/></svg></div>
<div class="contact-icon abs" style="left:559px;top:3091px"><svg width="26" height="30" viewBox="0 0 24 28" aria-hidden="true"><path d="M12 1a9 9 0 0 0-9 9c0 7 9 17 9 17s9-10 9-17a9 9 0 0 0-9-9zm0 12.5A3.5 3.5 0 1 1 12 6.5a3.5 3.5 0 0 1 0 7z" fill="#fff"/></svg></div>
<div class="contact-icon abs" style="left:888px;top:3091px"><svg width="28" height="22" viewBox="0 0 28 22" aria-hidden="true"><rect x="2" y="2" width="24" height="18" fill="none" stroke="#fff" stroke-width="2.5"/><polyline points="2,3 14,12 26,3" fill="none" stroke="#fff" stroke-width="2.5"/></svg></div>
<div class="contact-text abs" style="left:186px;top:3162px;width:200px">01632 960418</div>
<div class="contact-text abs" style="left:429px;top:3162px;width:320px">Unit 7, Harbour Point, Kestrel Road,<br>Meadowgate Business Park, Ashworth,<br>Wessex, AB1 2CD</div>
<div class="contact-text abs" style="left:788px;top:3162px;width:260px">info@brightfordcutworks.com</div>

<h3 class="quick-title abs display">Quick Contact</h3>
<nav class="footer-nav abs">
  <span style="left:265px">Home</span><span style="left:343px">|</span>
  <span style="left:384px">Materials</span><span style="left:489px">|</span>
  <span style="left:528px">Gallery</span><span style="left:618px">|</span>
  <span style="left:656px">Testimonials</span><span style="left:780px">|</span>
  <span style="left:820px">Contact us</span>
</nav>

<footer class="bottom-bar abs">
  Copyright © 2018&nbsp;<strong>BRIGHTFORD CUTWORKS</strong>. All Rights Reserved.
  <span class="social" style="left:896px"></span>
  <span class="social" style="left:935px"></span>
  <span class="social" style="left:974px"></span>
  <span class="social" style="left:1013px"></span>
  <span class="social" style="left:1052px"></span>
</footer>

</body>
</html>
```